Calendar Design

We are looking for a Calendar design for our 2025 calendar, We are R.T. Balford Construction Company. We pride our selves in Safety, Quality, and Production. Also we always "Make Safety Personal"
We are looking for a large one page wall hang calendar that shows all months in the year 2025 as a wall "Poster"
rtbalford.example for more information about us if needed

```html
<!DOCTYPE html>
<html lang="en">
<head>
<meta charset="utf-8">
<title>R.T. Balford Construction Company — 2025 Wall Calendar</title>
<link rel="stylesheet" href="https://fonts.googleapis.com/css2?family=Encode+Sans+Condensed:wght@400;600&family=Russo+One&family=Exo+2:ital,wght@0,800;1,800&display=swap">
<style>
  :root {
    --night: #0b1628;
    --steel: #24344c;
    --rust: #6a4a38;
    --panel: rgba(18, 20, 26, 0.62);
    --ink: #ffffff;
    --ink-soft: #e8e8ec;
  }
  * { margin: 0; padding: 0; box-sizing: border-box; }
  html, body { width: 1200px; height: 904px; overflow: hidden; background: var(--night); }
  .poster {
    position: relative; width: 1200px; height: 904px; overflow: hidden;
    font-family: "Encode Sans Condensed", "Arial Narrow", sans-serif; color: var(--ink);
  }
  .backdrop {
    position: absolute; inset: 0;
    background:
      radial-gradient(ellipse at 22% 35%, rgba(150,170,190,0.35), transparent 45%),
      radial-gradient(ellipse at 70% 70%, rgba(140,95,70,0.55), transparent 55%),
      linear-gradient(160deg, var(--night) 0%, var(--steel) 40%, var(--rust) 80%, #2a2624 100%);
  }
  .photo { position: absolute; }
  .photo-welder   { left: 478px; top: 29px; width: 211px; height: 127px; background: linear-gradient(135deg, #4f6a3a, #8a5a3c 55%, #5a2a24); }
  .photo-lift     { left: 701px; top: 29px; width: 225px; height: 127px; background: linear-gradient(180deg, #5f8fc4, #a8c2dc 45%, #8c7656 75%, #6c5a42); }
  .photo-row      { left: 936px; top: 29px; width: 225px; height: 127px; background: linear-gradient(160deg, #2f4a26, #5e6a3a 45%, #8a7456 80%); }
  .photo-spheres  { left: 38px; top: 748px; width: 267px; height: 126px; background: linear-gradient(180deg, #a7b6c8, #d6c4a6 55%, #b58a54 85%, #6a5a40); }
  .photo-station  { left: 324px; top: 748px; width: 200px; height: 126px; background: linear-gradient(170deg, #5a5e6a, #8a8e96 45%, #6a7a52 85%); }
  .photo-piping   { left: 543px; top: 748px; width: 200px; height: 126px; background: linear-gradient(170deg, #2e5e94, #d8dde4 50%, #9c9ea4 85%); }

  .brand { position: absolute; left: 38px; top: 28px; width: 380px; }
  .brand-name {
    font-family: "Exo 2", sans-serif; font-weight: 800; font-size: 64px; line-height: 1;
    letter-spacing: -1px; color: var(--ink); margin-top: 40px;
  }
  .brand-tagline {
    font-family: "Exo 2", sans-serif; font-weight: 800; font-style: italic;
    font-size: 21px; letter-spacing: 0.3px; color: var(--ink);
    position: absolute; top: 122px; left: 0; white-space: nowrap;
  }

  .calendar-panel {
    position: absolute; left: 426px; top: 175px; width: 735px; height: 553px;
    background: var(--panel); border-radius: 34px;
  }
  .year {
    position: absolute; left: 736px; top: 188px; width: 112px; text-align: center;
    font-family: "Russo One", sans-serif; font-size: 32px; letter-spacing: 1px; color: var(--ink);
  }
  .month { position: absolute; width: 165px; font-size: 11px; }
  .month h2 { font-weight: 600; font-size: 11.5px; height: 15px; line-height: 15px; }
  .month ol, .weekdays {
    display: grid; grid-template-columns: repeat(7, 22.8px); list-style: none;
  }
  .weekdays span, .month li { height: 15px; line-height: 15px; color: var(--ink-soft); }
  .weekdays span { font-weight: 600; }

  .jan { left: 448px; top: 238px; } .feb { left: 630px; top: 238px; }
  .mar { left: 812px; top: 238px; } .apr { left: 994px; top: 238px; }
  .may { left: 448px; top: 372px; } .jun { left: 630px; top: 372px; }
  .jul { left: 812px; top: 372px; } .aug { left: 994px; top: 372px; }
  .sep { left: 448px; top: 506px; } .oct { left: 630px; top: 506px; }
  .nov { left: 812px; top: 506px; } .dec { left: 994px; top: 506px; }

  .start-2 li:first-child { grid-column-start: 2; }
  .start-3 li:first-child { grid-column-start: 3; }
  .start-4 li:first-child { grid-column-start: 4; }
  .start-5 li:first-child { grid-column-start: 5; }
  .start-6 li:first-child { grid-column-start: 6; }
  .start-7 li:first-child { grid-column-start: 7; }

  .holidays { position: absolute; left: 448px; top: 640px; font-size: 11px; color: var(--ink-soft); }
  .holidays h3 { font-weight: 400; font-size: 11px; height: 15px; line-height: 15px; }
  .holiday-list {
    display: grid; grid-template-columns: 45px 114px 46px 114px 45px 91px 46px 120px;
    grid-auto-flow: column; grid-template-rows: repeat(3, 15px); line-height: 15px;
  }
  .holiday-list span { white-space: nowrap; }
</style>
</head>
<body>
<main class="poster">
  <div class="backdrop" role="img" aria-label="Night view of a lit refinery with large spherical storage tanks and piping"></div>

  <header class="brand">
    <h1 class="brand-name">R.T. Balford</h1>
    <p class="brand-tagline">SAFETY • QUALITY • PRODUCTION</p>
  </header>

  <div class="photo photo-welder" role="img" aria-label="Welder in protective gear welding a pipeline joint"></div>
  <div class="photo photo-lift" role="img" aria-label="Excavator lifting a pipe section on a cleared job site"></div>
  <div class="photo photo-row" role="img" aria-label="Coated pipe sections laid along a cleared right-of-way in the woods"></div>

  <section class="calendar-panel" aria-label="2025 calendar"></section>
  <p class="year">2025</p>

  <div class="month jan"><h2>January</h2><div class="weekdays"><span>Su</span><span>Mo</span><span>Tu</span><span>We</span><span>Th</span><span>Fr</span><span>Sa</span></div>
    <ol class="start-4"><li>1</li><li>2</li><li>3</li><li>4</li><li>5</li><li>6</li><li>7</li><li>8</li><li>9</li><li>10</li><li>11</li><li>12</li><li>13</li><li>14</li><li>15</li><li>16</li><li>17</li><li>18</li><li>19</li><li>20</li><li>21</li><li>22</li><li>23</li><li>24</li><li>25</li><li>26</li><li>27</li><li>28</li><li>29</li><li>30</li><li>31</li></ol></div>
  <div class="month feb"><h2>February</h2><div class="weekdays"><span>Su</span><span>Mo</span><span>Tu</span><span>We</span><span>Th</span><span>Fr</span><span>Sa</span></div>
    <ol class="start-7"><li>1</li><li>2</li><li>3</li><li>4</li><li>5</li><li>6</li><li>7</li><li>8</li><li>9</li><li>10</li><li>11</li><li>12</li><li>13</li><li>14</li><li>15</li><li>16</li><li>17</li><li>18</li><li>19</li><li>20</li><li>21</li><li>22</li><li>23</li><li>24</li><li>25</li><li>26</li><li>27</li><li>28</li></ol></div>
  <div class="month mar"><h2>March</h2><div class="weekdays"><span>Su</span><span>Mo</span><span>Tu</span><span>We</span><span>Th</span><span>Fr</span><span>Sa</span></div>
    <ol class="start-7"><li>1</li><li>2</li><li>3</li><li>4</li><li>5</li><li>6</li><li>7</li><li>8</li><li>9</li><li>10</li><li>11</li><li>12</li><li>13</li><li>14</li><li>15</li><li>16</li><li>17</li><li>18</li><li>19</li><li>20</li><li>21</li><li>22</li><li>23</li><li>24</li><li>25</li><li>26</li><li>27</li><li>28</li><li>29</li><li>30</li><li>31</li></ol></div>
  <div class="month apr"><h2>April</h2><div class="weekdays"><span>Su</span><span>Mo</span><span>Tu</span><span>We</span><span>Th</span><span>Fr</span><span>Sa</span></div>
    <ol class="start-3"><li>1</li><li>2</li><li>3</li><li>4</li><li>5</li><li>6</li><li>7</li><li>8</li><li>9</li><li>10</li><li>11</li><li>12</li><li>13</li><li>14</li><li>15</li><li>16</li><li>17</li><li>18</li><li>19</li><li>20</li><li>21</li><li>22</li><li>23</li><li>24</li><li>25</li><li>26</li><li>27</li><li>28</li><li>29</li><li>30</li></ol></div>

  <div class="month may"><h2>May</h2><div class="weekdays"><span>Su</span><span>Mo</span><span>Tu</span><span>We</span><span>Th</span><span>Fr</span><span>Sa</span></div>
    <ol class="start-5"><li>1</li><li>2</li><li>3</li><li>4</li><li>5</li><li>6</li><li>7</li><li>8</li><li>9</li><li>10</li><li>11</li><li>12</li><li>13</li><li>14</li><li>15</li><li>16</li><li>17</li><li>18</li><li>19</li><li>20</li><li>21</li><li>22</li><li>23</li><li>24</li><li>25</li><li>26</li><li>27</li><li>28</li><li>29</li><li>30</li><li>31</li></ol></div>
  <div class="month jun"><h2>June</h2><div class="weekdays"><span>Su</span><span>Mo</span><span>Tu</span><span>We</span><span>Th</span><span>Fr</span><span>Sa</span></div>
    <ol><li>1</li><li>2</li><li>3</li><li>4</li><li>5</li><li>6</li><li>7</li><li>8</li><li>9</li><li>10</li><li>11</li><li>12</li><li>13</li><li>14</li><li>15</li><li>16</li><li>17</li><li>18</li><li>19</li><li>20</li><li>21</li><li>22</li><li>23</li><li>24</li><li>25</li><li>26</li><li>27</li><li>28</li><li>29</li><li>30</li></ol></div>
  <div class="month jul"><h2>July</h2><div class="weekdays"><span>Su</span><span>Mo</span><span>Tu</span><span>We</span><span>Th</span><span>Fr</span><span>Sa</span></div>
    <ol class="start-3"><li>1</li><li>2</li><li>3</li><li>4</li><li>5</li><li>6</li><li>7</li><li>8</li><li>9</li><li>10</li><li>11</li><li>12</li><li>13</li><li>14</li><li>15</li><li>16</li><li>17</li><li>18</li><li>19</li><li>20</li><li>21</li><li>22</li><li>23</li><li>24</li><li>25</li><li>26</li><li>27</li><li>28</li><li>29</li><li>30</li><li>31</li></ol></div>
  <div class="month aug"><h2>August</h2><div class="weekdays"><span>Su</span><span>Mo</span><span>Tu</span><span>We</span><span>Th</span><span>Fr</span><span>Sa</span></div>
    <ol class="start-6"><li>1</li><li>2</li><li>3</li><li>4</li><li>5</li><li>6</li><li>7</li><li>8</li><li>9</li><li>10</li><li>11</li><li>12</li><li>13</li><li>14</li><li>15</li><li>16</li><li>17</li><li>18</li><li>19</li><li>20</li><li>21</li><li>22</li><li>23</li><li>24</li><li>25</li><li>26</li><li>27</li><li>28</li><li>29</li><li>30</li><li>31</li></ol></div>

  <div class="month sep"><h2>September</h2><div class="weekdays"><span>Su</span><span>Mo</span><span>Tu</span><span>We</span><span>Th</span><span>Fr</span><span>Sa</span></div>
    <ol class="start-2"><li>1</li><li>2</li><li>3</li><li>4</li><li>5</li><li>6</li><li>7</li><li>8</li><li>9</li><li>10</li><li>11</li><li>12</li><li>13</li><li>14</li><li>15</li><li>16</li><li>17</li><li>18</li><li>19</li><li>20</li><li>21</li><li>22</li><li>23</li><li>24</li><li>25</li><li>26</li><li>27</li><li>28</li><li>29</li><li>30</li></ol></div>
  <div class="month oct"><h2>October</h2><div class="weekdays"><span>Su</span><span>Mo</span><span>Tu</span><span>We</span><span>Th</span><span>Fr</span><span>Sa</span></div>
    <ol class="start-4"><li>1</li><li>2</li><li>3</li><li>4</li><li>5</li><li>6</li><li>7</li><li>8</li><li>9</li><li>10</li><li>11</li><li>12</li><li>13</li><li>14</li><li>15</li><li>16</li><li>17</li><li>18</li><li>19</li><li>20</li><li>21</li><li>22</li><li>23</li><li>24</li><li>25</li><li>26</li><li>27</li><li>28</li><li>29</li><li>30</li><li>31</li></ol></div>
  <div class="month nov"><h2>November</h2><div class="weekdays"><span>Su</span><span>Mo</span><span>Tu</span><span>We</span><span>Th</span><span>Fr</span><span>Sa</span></div>
    <ol class="start-7"><li>1</li><li>2</li><li>3</li><li>4</li><li>5</li><li>6</li><li>7</li><li>8</li><li>9</li><li>10</li><li>11</li><li>12</li><li>13</li><li>14</li><li>15</li><li>16</li><li>17</li><li>18</li><li>19</li><li>20</li><li>21</li><li>22</li><li>23</li><li>24</li><li>25</li><li>26</li><li>27</li><li>28</li><li>29</li><li>30</li></ol></div>
  <div class="month dec"><h2>December</h2><div class="weekdays"><span>Su</span><span>Mo</span><span>Tu</span><span>We</span><span>Th</span><span>Fr</span><span>Sa</span></div>
    <ol class="start-2"><li>1</li><li>2</li><li>3</li><li>4</li><li>5</li><li>6</li><li>7</li><li>8</li><li>9</li><li>10</li><li>11</li><li>12</li><li>13</li><li>14</li><li>15</li><li>16</li><li>17</li><li>18</li><li>19</li><li>20</li><li>21</li><li>22</li><li>23</li><li>24</li><li>25</li><li>26</li><li>27</li><li>28</li><li>29</li><li>30</li><li>31</li></ol></div>

  <section class="holidays">
    <h3>Federal Holidays 2025</h3>
    <div class="holiday-list">
      <span>Jan 1</span><span>Jan 20</span><span>Feb 17</span>
      <span>New Year's Day</span><span>Martin Luther King Day</span><span>Presidents' Day</span>
      <span>May 26</span><span>Jun 19</span><span>Jul 4</span>
      <span>Memorial Day</span><span>Juneteenth</span><span>Independence Day</span>
      <span>Sep 1</span><span>Oct 13</span><span>Nov 11</span>
      <span>Labor Day</span><span>Columbus Day</span><span>Veterans Day</span>
      <span>Nov 27</span><span>Dec 25</span><span></span>
      <span>Thanksgiving Day</span><span>Christmas Day</span><span></span>
    </div>
  </section>

  <div class="photo photo-spheres" role="img" aria-label="Row of white spherical gas storage tanks at sunset"></div>
  <div class="photo photo-station" role="img" aria-label="Aerial view of a gas compressor station with piping"></div>
  <div class="photo photo-piping" role="img" aria-label="Large white above-ground pipeline bends at a facility under blue sky"></div>
</main>
</body>
</html>
```